Varro's Electrical & Solar Corflute Signage Design

So my plan is to put this design onto a 600 by 400 corflute sign (this sign will be printed out and cable tied to a fence FYI). I would like to have the name and the icon stand out. I need Varro's Electrical & Solar to be big and clear and I would like to have my "S" icon faded behind "Varro's Electrical & Solar" in the background.

I want to have my Lic No. - Top left with my ABN directly underneath. (I Want two ticks infront of them like this)
✓ Lic No. 582164K
✓ ABN 41 276 519 683

I want to have written on it: ALL ASPECTS OF ELECTRICAL (please use cool fonts and nothing too plain)
I also want to have: YOUR LOCAL TRUSTED ELECTRICIAN but if it looks too dicky then just have "all aspects of electrical" and just "free quotes • fast service" somewhere.
Directly underneath (smaller but still clear): FREE QUOTES • FAST SERVICE

At the bottom, I need my phone number big and clear - 0438 617 905 I would like this on a banner meaning like a cool strip at the bottom. (Please make the strip/banner look cool and not boring. Maybe shade the colour or something)
I also want the Facebook & Instagram icons on there so people can look us up on facebook & Instagram (make them match the colour of my logo or you could try any other colour that works)
Thank you so much!!

Colors

Designer to choose colors to be used in the design.

Requirements
Should not have
• no different colours other then the colours on my logo and icon

```html
<!DOCTYPE html>
<html lang="en">
<head>
<meta charset="utf-8">
<title>Varro's Electrical &amp; Solar – Corflute Sign</title>
<link rel="stylesheet" href="https://fonts.googleapis.com/css2?family=Montserrat:wght@700;800;900&display=swap">
<style>
  :root {
    --green: #1aa33a;
    --green-deep: #0e8a2d;
    --green-light: #acd6a0;
    --green-bright: #5bbb48;
    --charcoal: #232a33;
    --silver-light: #eceef1;
    --silver-mid: #c9ccd2;
    --silver-dark: #7d8792;
    --white: #ffffff;
  }
  * { margin: 0; padding: 0; box-sizing: border-box; }
  html, body { width: 1200px; height: 841px; overflow: hidden; background: #ffffff; }
  .sign {
    position: relative; width: 1200px; height: 841px; overflow: hidden;
    background: var(--white);
    font-family: "Montserrat", Arial, sans-serif;
  }
  .backdrop { position: absolute; inset: 0; }
  .brand-name {
    position: absolute; left: 0; width: 1200px; top: 46px;
    text-align: center; color: var(--green); font-weight: 900; line-height: 1;
  }
  .brand-name .brand-main { display: block; font-size: 150px; letter-spacing: 4px; }
  .brand-name .brand-sub { display: block; font-size: 30px; letter-spacing: 22px; margin-top: 4px; }
  .headline {
    position: absolute; left: 54px; top: 268px; width: 1092px;
    font-weight: 800; font-size: 91px; line-height: 1;
    color: var(--green); white-space: nowrap;
    background: linear-gradient(180deg, #12a232 0%, #23b23c 45%, #6cc45a 55%, #19a436 100%);
    -webkit-background-clip: text; background-clip: text; -webkit-text-fill-color: transparent;
  }
  .tagline {
    position: absolute; left: 57px; top: 362px;
    font-weight: 800; font-size: 72.5px; line-height: 1; color: var(--charcoal); white-space: nowrap;
  }
  .offer {
    position: absolute; left: 57px; top: 488px;
    font-weight: 800; font-size: 43px; line-height: 52px; color: var(--charcoal);
  }
  .credentials {
    position: absolute; left: 54px; top: 614px;
    font-weight: 800; font-size: 40px; line-height: 47px; letter-spacing: -1px;
    color: var(--white); -webkit-text-stroke: 5px var(--charcoal); paint-order: stroke fill;
    white-space: nowrap;
  }
  .credentials .label-green { color: var(--green-bright); }
  .phone {
    position: absolute; left: 52px; top: 704px;
    font-weight: 900; font-size: 100px; line-height: 1; letter-spacing: -4px;
    color: var(--green); -webkit-text-stroke: 9px var(--charcoal); paint-order: stroke fill;
    white-space: nowrap;
  }
  .social { position: absolute; left: 749px; top: 758px; display: flex; gap: 12px; }
  .social-dot { width: 26px; height: 26px; border-radius: 50%; background: var(--charcoal); }
  .emblem { position: absolute; left: 800px; top: 468px; width: 340px; height: 340px; }
</style>
</head>
<body>
<main class="sign">
  <svg class="backdrop" width="1200" height="841" viewBox="0 0 1200 841" aria-hidden="true">
    <defs>
      <linearGradient id="silverSweep" x1="0" y1="0" x2="1" y2="0">
        <stop offset="0" stop-color="#c6c9cf"/>
        <stop offset="0.35" stop-color="#eef0f2"/>
        <stop offset="0.7" stop-color="#dfe1e5"/>
        <stop offset="1" stop-color="#c9ccd2"/>
      </linearGradient>
      <linearGradient id="panelSilver" x1="0" y1="0" x2="1" y2="0">
        <stop offset="0" stop-color="#d4d7dc"/>
        <stop offset="0.5" stop-color="#eceef1"/>
        <stop offset="1" stop-color="#7d8792"/>
      </linearGradient>
    </defs>
    <polygon class="silver-bolt" fill="url(#silverSweep)"
      points="0,392 590,392 470,470 870,404 806,540 1200,520 512,713 588,544 0,544"/>
    <polygon class="green-corner" fill="var(--green-light)" points="0,392 65,477 0,477"/>
    <polygon class="green-field" fill="var(--green-light)"
      points="0,544 588,544 512,713 1200,520 1200,841 0,841"/>
    <polygon class="offer-panel" fill="url(#panelSilver)" points="0,477 512,477 440,600 0,600"/>
    <polyline class="offer-panel-edge" fill="none" stroke="var(--green-bright)" stroke-width="4"
      points="512,477 440,600 0,600"/>
  </svg>

  <h1 class="brand-name">
    <span class="brand-main">VARRO'S</span>
    <span class="brand-sub">ELECTRICAL &amp; SOLAR</span>
  </h1>

  <p class="headline">ELECTRICAL &amp; SOLAR</p>
  <p class="tagline">ALL ASPECTS OF ELECTRICA</p>

  <p class="offer">FREE QUOTES &amp;<br>FAST SERVICE</p>

  <p class="credentials">
    <span class="label-green">Lic No.</span> 582164K<br>
    ABN 41 276 519 683
  </p>

  <p class="phone">0438 617 905</p>

  <div class="social" role="img" aria-label="Social media links">
    <span class="social-dot"></span>
    <span class="social-dot"></span>
    <span class="social-dot"></span>
  </div>

  <svg class="emblem" viewBox="0 0 340 340" role="img" aria-label="Varro's emblem">
    <circle cx="170" cy="170" r="156" fill="none" stroke="var(--green)" stroke-width="14"/>
    <text x="170" y="186" text-anchor="middle" font-family="Montserrat, Arial, sans-serif"
      font-weight="900" font-size="50" fill="var(--green)">VARRO'S</text>
  </svg>
</main>
</body>
</html>
```